Business Card Design - Pediatric Dentist

We need a business card for a new dental office. We are a pediatric dentist in Austin Tx. I would like a design that use bright green and if possible light blue.

Target Market(s)

Marketed to young moms

Industry/Entity Type

Dental

Contact Information for Business Card

Marcus Hollin DDS
Tidewell Pediatric Dentistry
438 E. Corvell Lane. Austin TX 78731
(512) 284 9153.

In the back i would like to state "we take most insurances, Chip & Medicaid" & a map

Colors
add136
cadf82
85cae6

```html
<!DOCTYPE html>
<html lang="en">
<head>
<meta charset="utf-8">
<title>Tidewell Pediatric Dentistry – Business Card</title>
<link rel="stylesheet" href="https://fonts.googleapis.com/css2?family=Tinos&family=Questrial&display=swap">
<style>
  :root {
    --bright-green: #2fa83a;
    --mark-green: #add136;
    --sky-blue: #c9e0f2;
    --card-white: #ffffff;
    --ink: #111111;
    --backdrop: #eef1f3;
  }
  * { margin: 0; padding: 0; box-sizing: border-box; }
  html, body { width: 1200px; height: 784px; overflow: hidden; }
  body {
    background: var(--backdrop);
    position: relative;
    font-family: "Tinos", "Times New Roman", serif;
    color: var(--ink);
  }
  .card {
    position: absolute;
    width: 600px;
    height: 343px;
    background: linear-gradient(180deg, var(--sky-blue) 0%, #e4f0f9 55%, var(--card-white) 100%);
    box-shadow: 0 6px 18px rgba(0,0,0,0.18);
    overflow: hidden;
  }
  .card-front { left: 50px; top: 40px; }
  .card-back { left: 550px; top: 400px; }

  .brand { position: absolute; display: flex; align-items: center; }
  .brand-dot {
    border-radius: 50%;
    background: var(--bright-green);
    flex: none;
  }
  .brand-name { line-height: 1.02; color: var(--ink); font-weight: 400; }

  .card-front .brand { left: 60px; top: 40px; gap: 34px; }
  .card-front .brand-dot { width: 180px; height: 180px; }
  .card-front .brand-name { font-size: 50px; }

  .card-back .brand { left: 48px; top: 26px; gap: 22px; }
  .card-back .brand-dot { width: 100px; height: 100px; }
  .card-back .brand-name { font-size: 31px; }

  .rule-thin {
    position: absolute; left: 290px; right: 0; top: 118px;
    height: 12px; background: var(--bright-green);
  }
  .insurance-band {
    position: absolute; left: 0; right: 0; top: 150px;
    height: 30px; background: var(--bright-green);
    display: flex; align-items: center; padding-left: 48px;
    font-family: "Questrial", "Century Gothic", sans-serif;
    font-size: 19px; letter-spacing: 2.5px; color: var(--card-white);
  }
  .dentist-name {
    position: absolute; left: 58px; top: 192px;
    font-size: 21px; color: var(--bright-green);
  }
  .contact { position: absolute; left: 58px; top: 238px; font-size: 21px; line-height: 1.3; list-style: none; }
</style>
</head>
<body>
  <section class="card card-front" aria-label="Card front">
    <div class="brand">
      <span class="brand-dot" aria-hidden="true"></span>
      <h1 class="brand-name">Tidewell<br>Pediatric<br>Dentistry</h1>
    </div>
  </section>

  <section class="card card-back" aria-label="Card back">
    <div class="brand">
      <span class="brand-dot" aria-hidden="true"></span>
      <h2 class="brand-name">Tidewell<br>Pediatric<br>Dentistry</h2>
    </div>
    <div class="rule-thin" aria-hidden="true"></div>
    <p class="insurance-band">we take most insurances, Chip &amp; Medicaid</p>
    <p class="dentist-name">Marcus Hollin DDS</p>
    <ul class="contact">
      <li>(512) 284 9153</li>
      <li>Tidewell Pediatric Dentistry</li>
      <li>438 E. Corvell Lane. Austin TX 78731</li>
    </ul>
  </section>
</body>
</html>
```